TWR Handyman Service

File 2 Prep kitchen cabinets
File 3 Painting kitchen cabinets
File 4 Demo stairs
File 5 Completion Installing stair treads
File 6 Power washing deck
File 7 Completion of Sainting deck and railings
File 8 Completion of staining steps
Logo, owner name, email and web site on front cover
File 9 Demo living room floor
File 10 Completion of living room floor
Please see additional on attached flyer

Target Market(s)

Residential

Industry/Entity Type

Painting

Font styles to use
Serif
Sans Serif

Requirements
Must have
• Some Photos and type of work discerption
Front page Logo, web address, phone number, owners name and email address
Back Page see attached file 1
Nice to have
• Photo maybe in middle of flyer
Use the best text that you think will meet the needs
Should not have
• No pink colors

```html
<!DOCTYPE html>
<html lang="en">
<head>
<meta charset="utf-8">
<title>TWR Handyman Services – Services Flyer</title>
<link href="https://fonts.googleapis.com/css2?family=Arimo:wght@400;700&display=swap" rel="stylesheet">
<style>
  :root {
    --stage: #262628;
    --paper: #ffffff;
    --ink: #333333;
    --mist: #e8e9e9;
    --slate: #b1b2b4;
    --brand-blue: #3e62a8;
    --on-blue: #ffffff;
  }
  * { box-sizing: border-box; margin: 0; padding: 0; }
  html, body { width: 1200px; height: 921px; overflow: hidden; background: var(--stage); }
  body { position: relative; font-family: "Arimo", Arial, sans-serif; color: var(--ink); }

  .flyer { position: absolute; left: 91px; top: 67px; width: 1018px; height: 787px; background: var(--paper); overflow: hidden; }
  .block { position: absolute; }
  .photo { position: absolute; }

  .mist-tile { left: 540px; top: 0; width: 139px; height: 192px; background: var(--mist); }
  .slate-panel { left: 679px; top: 0; width: 339px; height: 466px; background: var(--slate); }
  .brand-panel { left: 0; top: 595px; width: 336px; height: 192px; background: var(--brand-blue); display: flex; align-items: center; justify-content: center; }
  .mission-panel { left: 679px; top: 466px; width: 339px; height: 321px; background: var(--brand-blue); }

  .photo-painting-room { left: 0; top: 0; width: 336px; height: 192px; background: linear-gradient(135deg, #efe6da 0%, #c9ad8e 55%, #8e6b52 100%); }
  .photo-stair-demo { left: 343px; top: 0; width: 189px; height: 192px; background: linear-gradient(160deg, #ddd6c4 0%, #b2a58d 60%, #6f6a63 100%); }
  .photo-garage { left: 709px; top: 18px; width: 131px; height: 174px; background: linear-gradient(180deg, #a9c4dc 0%, #d9b78f 45%, #5f9a3c 70%, #4c8a2f 100%); }
  .photo-back-door { left: 855px; top: 18px; width: 131px; height: 174px; background: linear-gradient(180deg, #c4ccd6 0%, #6a7f98 50%, #7a3a24 85%, #8c4a2f 100%); }
  .photo-hallway { left: 540px; top: 199px; width: 139px; height: 121px; background: linear-gradient(150deg, #e6dcc8 0%, #b9ab93 55%, #8b8780 100%); }
  .photo-floor { left: 540px; top: 328px; width: 139px; height: 131px; background: linear-gradient(160deg, #c8c7c4 0%, #a6a4a0 50%, #8d8b88 100%); }
  .photo-cabinet-prep { left: 540px; top: 466px; width: 139px; height: 121px; background: linear-gradient(180deg, #ece6d8 0%, #b58b5c 55%, #3a5e8c 100%); }
  .photo-kitchen { left: 343px; top: 595px; width: 189px; height: 192px; background: linear-gradient(180deg, #f1e6c4 0%, #5b626c 45%, #d9d2c0 100%); }
  .photo-cabinet-paint { left: 540px; top: 595px; width: 139px; height: 192px; background: linear-gradient(180deg, #ece7dc 0%, #b08a64 45%, #bdbab3 100%); }

  .service { position: absolute; list-style: none; }
  .service-title { position: relative; font-size: 18px; font-weight: 700; line-height: 22px; margin-bottom: 2px; }
  .service-title::before { content: ""; position: absolute; left: -17px; top: 8px; width: 7px; height: 7px; border-radius: 50%; background: var(--ink); }
  .service-item { font-size: 13.4px; line-height: 20.5px; }

  .interior { left: 79px; top: 219px; }
  .exterior { left: 79px; top: 382px; }
  .carpentry { left: 392px; top: 219px; width: 140px; }
  .carpentry .service-title { margin-bottom: 3px; }
  .carpentry .service-item { line-height: 16px; margin-bottom: 4.5px; }
  .maintenance { left: 747px; top: 219px; }

  .brand-name { color: var(--on-blue); font-size: 18px; font-weight: 700; }

  .mission { position: absolute; left: 726px; top: 500px; width: 238px; color: var(--on-blue); }
  .mission-title { font-size: 17px; font-weight: 700; line-height: 22px; margin-bottom: 2px; }
  .mission-text { font-size: 13.2px; line-height: 17.4px; }
</style>
</head>
<body>
<main class="flyer">
  <div class="block mist-tile"></div>
  <div class="block slate-panel"></div>
  <div class="block brand-panel">
    <p class="brand-name">TWR Handyman Services</p>
  </div>
  <div class="block mission-panel"></div>

  <div class="photo photo-painting-room" role="img" aria-label="Living room covered in plastic sheeting with a ladder, ready for interior painting"></div>
  <div class="photo photo-stair-demo" role="img" aria-label="Staircase during demolition before new stair treads"></div>
  <div class="photo photo-garage" role="img" aria-label="Completed garage addition with lawn in front"></div>
  <div class="photo photo-back-door" role="img" aria-label="New sliding door with freshly stained steps and white railings"></div>
  <div class="photo photo-hallway" role="img" aria-label="Hallway with new flooring leading to the front door"></div>
  <div class="photo photo-floor" role="img" aria-label="Completed grey plank living room floor"></div>
  <div class="photo photo-cabinet-prep" role="img" aria-label="Kitchen cabinets taped and prepped for painting"></div>
  <div class="photo photo-kitchen" role="img" aria-label="Kitchen with newly painted dark grey cabinets"></div>
  <div class="photo photo-cabinet-paint" role="img" aria-label="Cabinet frames painted white over drop cloths"></div>

  <ul class="service interior">
    <li class="service-title">Interior Painting</li>
    <li class="service-item">Commercial &amp; Residential</li>
    <li class="service-item">Kitchen Cabinets</li>
    <li class="service-item">Painting</li>
    <li class="service-item">Walls trim &amp; doors</li>
    <li class="service-item">Celling repair</li>
    <li class="service-item">Staining &amp; polying trim</li>
  </ul>

  <ul class="service exterior">
    <li class="service-title">Exterior Painting</li>
    <li class="service-item">Commercial &amp; Residential</li>
    <li class="service-item">New Painting &amp; Updates</li>
    <li class="service-item">All types of Siding</li>
    <li class="service-item">Power washing</li>
    <li class="service-item">Painting &amp; Staining of decks</li>
    <li class="service-item">Fence cleaning painting &amp; sealing</li>
    <li class="service-item">Furniture cleaning, painting &amp; sealing</li>
  </ul>

  <ul class="service carpentry">
    <li class="service-title">Carpentry</li>
    <li class="service-item">Commercial &amp;<br>Residential</li>
    <li class="service-item">Kitchen remodeling</li>
    <li class="service-item">Marble &amp; Granite<br>countertops</li>
    <li class="service-item">Bathroom<br>remodeling</li>
    <li class="service-item">Basement<br>remodeling</li>
    <li class="service-item">Disabled accessible<br>ramps &amp; bathroom<br>installation</li>
    <li class="service-item">Room additions</li>
    <li class="service-item">All types of siding</li>
    <li class="service-item">Cabinetry</li>
    <li class="service-item">Sheet rocking</li>
  </ul>

  <ul class="service maintenance">
    <li class="service-title">Maintenance</li>
    <li class="service-item">Commercial &amp; Residential</li>
    <li class="service-item">Hanging Curtin's &amp; Blinds</li>
    <li class="service-item">Shelving</li>
    <li class="service-item">Lighting</li>
    <li class="service-item">Picture hanging</li>
    <li class="service-item">TV mounting</li>
    <li class="service-item">Desk &amp; furniture assembly</li>
    <li class="service-item">Fixture installation &amp; repair</li>
    <li class="service-item">Clean out basement &amp; storage areas</li>
  </ul>

  <section class="mission">
    <h2 class="mission-title">The Mission</h2>
    <p class="mission-text">At TWR Handyman Services we are committed to client satisfaction and understanding that customer service is the foundation of our business. We are dedicated to providing our clients with quality workmanship performed in a prompt, professional manner. Our reliable team, second to non, will arrive neat in appearance and ready to work. Our technicians will treat each job, large or small, with the same care we would if we were repairing our own home.</p>
  </section>
</main>
</body>
</html>
```